Gilded Reef / Alcoholic Drink, Brochure design

We are in need of a design for our all natural, low calorie, organically sweetened alcoholic drink. Our drink is currently a frozen mixed drink similar to a margarita and has the taste of real fruit. It is targeted to high end, midrange, and lower end resorts and hotels through Mexico. It will eventually enter the U.S. market within one year in the form of both the frozen and canned and bottled ready to drink. Some things to include in the brochure are:

Welcome to the harmonious and flavorful, world of Gilded Reef. Encounter the bold, real fruit taste of an exceptional drink that is organically sweetened, all natural, low in calories with a refreshing, smooth finish. Gilded Reef uses ultra premium ingredients and distilled by a process so pure, that it delivers a smooth, full, balanced taste with no bitter after burn. So, on hot summer days and steamy nights join us for the one of a kind experience of Gilded Reef.

-All Natural, real fruit
-Organically sweetened
-Low Calorie
-Bottled at the Source
-Solid revenues
-High profit margin

Target Market(s)

Resort managers, purchasers. Their market is 25-50 age range males and females who vacation at cities in Mexico like Cancun, Puerta Vallarta.

Font styles to use
Sans Serif

Requirements
Must have
• Clean, modern, upscale design
• Why you should consider Gilded Reef for your business. In the rapidly growing market of organic foods and healthy choices, Gilded Reef is a leader in the alcohol industry on this phenomena. Our ultra premium, all natural, low calorie ingredients are perfect for this exponentially expanding market in the U.S., Europe and beyond. Whether your establishment is a corporate all inclusive resort destination, a midrange one or just one owned by an individual, we've designed Gilded Reef to keep you within a highly profitable margin - thus making you money.
• Frozen-
• Crafted and bottled at the source.
• No guesswork in adding liquor, just pour, freeze and serve.
• A large selection of real fruit flavors.
• Two different ABV percentages to choose from 5% and "Gilded Summit" at 8%.
• Ready to Drink-
• Crafted and bottled at the source
• Carbonated for the ultimate in refreshment
• Available in both glass and aluminum

```html
<!DOCTYPE html>
<html lang="en">
<head>
<meta charset="utf-8">
<title>Gilded Reef – Brochure Layout</title>
<link href="https://fonts.googleapis.com/css2?family=Questrial&family=Arimo&display=swap" rel="stylesheet">
<style>
  :root {
    --board: #b4b5b9;
    --ink-black: #000000;
    --paper: #ffffff;
    --sky-blue: #5cb8e6;
    --stripe-orange: #d8612a;
    --stripe-blue: #5fb6e0;
    --body-grey: #8a8c90;
    --label-red: #e0201c;
    --soft-white: #e8e8e8;
    --watermark: #1f2529;
  }
  * { box-sizing: border-box; margin: 0; padding: 0; }
  html, body { width: 1200px; height: 1000px; overflow: hidden; }
  body {
    background: var(--board);
    font-family: "Questrial", "Century Gothic", sans-serif;
    position: relative;
  }
  .board-label {
    position: absolute;
    font-family: "Arimo", Arial, sans-serif;
    font-size: 21px;
    color: var(--label-red);
  }
  .panel { position: absolute; overflow: hidden; }
  .panel--black { background: var(--ink-black); }
  .panel--white { background: var(--paper); }
  .photo { position: absolute; left: 0; width: 100%; }
  .stripes { position: absolute; left: 0; width: 100%; height: 8px; }
  .stripes::before, .stripes::after { content: ""; position: absolute; left: 0; width: 100%; height: 4px; }
  .stripes::before { top: 0; background: var(--stripe-orange); }
  .stripes::after { top: 4px; background: var(--stripe-blue); }
  .brand-name { position: absolute; color: var(--sky-blue); line-height: 1; white-space: nowrap; font-weight: 400; }

  /* cover */
  .cover { left: 190px; top: 38px; width: 210px; height: 447px; }
  .cover .photo { top: 0; height: 217px; background: linear-gradient(180deg, #3a3a3a 0%, #6e6e6e 45%, #2c2c2c 100%); }
  .cover .stripes { top: 217px; }
  .cover .brand-name { left: 0; width: 100%; text-align: center; top: 280px; font-size: 24px; }
  .cover-welcome { position: absolute; left: 70px; top: 363px; width: 135px; font-size: 12.5px; line-height: 15.5px; color: var(--soft-white); }
  .cover-welcome span { color: var(--sky-blue); }

  /* intro white panel (shared) */
  .intro .brand-name { left: 40px; top: 40px; font-size: 12px; color: #6a8fa6; }
  .intro-lead { position: absolute; left: 39px; top: 121px; font-size: 11px; line-height: 14.5px; color: var(--body-grey); white-space: nowrap; letter-spacing: -0.1px; }
  .intro-body { position: absolute; left: 39px; top: 206px; font-size: 6.2px; line-height: 8.6px; color: var(--body-grey); white-space: nowrap; }
  .intro .photo { bottom: 0; height: 137px; background: radial-gradient(ellipse at 50% 55%, #b89134 0%, #5c4a2a 18%, #2e2a26 45%, #151515 100%); }
  .intro .stripes { bottom: 137px; }

  .intro--page { left: 555px; top: 37px; width: 213px; height: 446px; }
  .intro--inside { left: 108px; top: 517px; width: 210px; height: 446px; }
  .intro--inside .intro-lead { top: 125px; }
  .intro--inside .intro-body { top: 208px; }

  /* benefits panel */
  .benefits { left: 768px; top: 35px; width: 207px; height: 452px; }
  .benefits .photo { top: 168px; height: 137px; background: linear-gradient(100deg, #8f8a80 0%, #6b6259 40%, #3f3a35 75%, #6a6f72 100%); }
  .benefits .stripes { top: 305px; }
  .benefit-list { position: absolute; left: 62px; list-style: none; }
  .benefit-list li { position: relative; font-size: 10.5px; color: var(--soft-white); height: 28px; line-height: 14px; }
  .benefit-list li::before { content: ""; position: absolute; left: -10px; top: 4px; width: 6px; height: 6px; border-radius: 50%; background: var(--sky-blue); }
  .benefit-list--top { top: 69px; }
  .benefit-list--bottom { top: 342px; }

  /* inside: pitch panel */
  .pitch { left: 318px; top: 517px; width: 210px; height: 446px; }
  .pitch .photo { top: 0; height: 163px; background: linear-gradient(180deg, #c9c6bf 0%, #7d7a73 35%, #4a4640 70%, #2a2826 100%); }
  .pitch .stripes { top: 163px; }
  .pitch-heading { position: absolute; left: 32px; top: 205px; color: var(--soft-white); font-size: 13px; line-height: 16px; font-weight: 400; }
  .pitch-heading .pitch-brand { display: block; color: var(--sky-blue); font-size: 19.5px; line-height: 26px; }
  .pitch-heading .pitch-tail { display: block; font-size: 15.5px; line-height: 20px; }
  .pitch-copy { position: absolute; left: 32px; width: 150px; font-size: 6.2px; line-height: 8.6px; color: #d0d0d0; }
  .pitch-copy--one { top: 286px; }
  .pitch-copy--two { top: 360px; }

  /* inside: range panel */
  .range { left: 528px; top: 517px; width: 212px; height: 446px; background: linear-gradient(90deg, #c9c9c9 0%, #f2f2f2 10%, #ffffff 20%); }
  .range-title { position: absolute; left: 38px; font-size: 13px; color: var(--sky-blue); font-weight: 400; }
  .range-title--frozen { top: 52px; }
  .range-title--ready { top: 156px; }
  .range-list { position: absolute; left: 38px; width: 145px; list-style: none; font-size: 6.4px; line-height: 7.7px; color: var(--body-grey); }
  .range-list li { position: relative; padding-left: 5px; }
  .range-list li::before { content: ""; position: absolute; left: -2px; top: 3px; width: 3px; height: 3px; border-radius: 50%; background: var(--sky-blue); }
  .range-list--frozen { top: 74px; }
  .range-list--ready { top: 178px; }
  .range .photo { left: 10px; width: 192px; top: 272px; height: 172px; background: linear-gradient(90deg, #e06a1c 0%, #e06a1c 24%, #e39428 26%, #e39428 49%, #8fd35a 51%, #8fd35a 74%, #dcdcdc 76%, #dcdcdc 100%); opacity: 0.85; }

  /* back */
  .back { left: 838px; top: 517px; width: 210px; height: 446px; }
  .back .photo { top: 0; height: 216px; background: linear-gradient(180deg, #4f96d8 0%, #a9d2ef 45%, #d8dfe0 70%, #e9dcc2 100%); }
  .back .stripes { top: 216px; }
  .back .brand-name { left: 0; width: 100%; text-align: center; top: 400px; font-size: 30px; color: var(--watermark); }
  .back-contacts { position: absolute; left: 58px; top: 334px; font-size: 11px; line-height: 16px; color: var(--soft-white); letter-spacing: 0.2px; }
</style>
</head>
<body>

  <p class="board-label" style="left:69px; top:271px;">cover</p>
  <p class="board-label" style="left:1010px; top:257px;">1 “page”</p>
  <p class="board-label" style="left:19px; top:750px;">inside</p>
  <p class="board-label" style="left:1092px; top:733px;">back</p>

  <!-- Cover -->
  <section class="panel panel--black cover">
    <div class="photo" role="img" aria-label="Black and white photo of a group of young friends walking together at night"></div>
    <div class="stripes"></div>
    <p class="brand-name">Gilded Reef</p>
    <p class="cover-welcome">Welcome to the harmonious and flavorful, world of <span>Gilded Reef.</span></p>
  </section>

  <!-- Single page: intro -->
  <section class="panel panel--white intro intro--page">
    <p class="brand-name">Gilded Reef</p>
    <p class="intro-lead">Encounter the bold, real fruit<br>taste of an exceptional drink<br>that is organically sweetened,<br>all natural, low in calories with<br>a refreshing, smooth finish.</p>
    <p class="intro-body">Gilded Reef uses ultra premium ingredients<br>and distilled by a process so pure, that it<br>delivers a smooth, full, balanced taste<br>with no bitter after burn. So, on hot summer<br>days and steamy nights join us for the one<br>of a kind experience of Gilded Reef.</p>
    <div class="stripes"></div>
    <div class="photo" role="img" aria-label="Photo of a glass of golden frozen drink with a straw on a bar table"></div>
  </section>

  <!-- Single page: benefits -->
  <section class="panel panel--black benefits">
    <ul class="benefit-list benefit-list--top">
      <li>All Natural, real fruit</li>
      <li>Organically sweetened</li>
      <li>Low Calorie</li>
    </ul>
    <div class="photo" role="img" aria-label="Photo of a couple chatting on a sunny beach"></div>
    <div class="stripes"></div>
    <ul class="benefit-list benefit-list--bottom">
      <li>Bottled at the Source</li>
      <li>Solid revenues</li>
      <li>High profit margin</li>
    </ul>
  </section>

  <!-- Inside spread: intro -->
  <section class="panel panel--white intro intro--inside">
    <p class="brand-name">Gilded Reef</p>
    <p class="intro-lead">Encounter the bold, real fruit<br>taste of an exceptional drink<br>that is organically sweetened,<br>all natural, low in calories with<br>a refreshing, smooth finish.</p>
    <p class="intro-body">Gilded Reef uses ultra premium ingredients<br>and distilled by a process so pure, that it<br>delivers a smooth, full, balanced taste<br>with no bitter after burn. So, on hot summer<br>days and steamy nights join us for the one<br>of a kind experience of Gilded Reef.</p>
    <div class="stripes"></div>
    <div class="photo" role="img" aria-label="Photo of a glass of golden frozen drink with a straw on a bar table"></div>
  </section>

  <!-- Inside spread: pitch -->
  <section class="panel panel--black pitch">
    <div class="photo" role="img" aria-label="Photo of friends relaxing together at a seaside resort"></div>
    <div class="stripes"></div>
    <h2 class="pitch-heading">Why you should consider <span class="pitch-brand">Gilded Reef</span><span class="pitch-tail">for your company?</span></h2>
    <p class="pitch-copy pitch-copy--one">In the rapidly growing market of organic foods and healthy choices, GR is a leader in the alcohol industry on this phenomena. Our ultra premium, all natural, low calorie ingredients are perfect for this exponentially expanding market in the U.S., Europe and beyond.</p>
    <p class="pitch-copy pitch-copy--two">Whether your establishment is a corporate all inclusive resort destination, a midrange one or just one owned by an individual, we’ve designed Gilded Reef to keep you within a highly profitable margin - thus making you money.</p>
  </section>

  <!-- Inside spread: range -->
  <section class="panel range">
    <h3 class="range-title range-title--frozen">Frozen</h3>
    <ul class="range-list range-list--frozen">
      <li>Crafted and bottled at the source.</li>
      <li>No guesswork in adding liquor,<br>just pour, freeze and serve.</li>
      <li>A large selection of real fruit flavors.</li>
      <li>Two different ABV percentages to<br>choose from 5% and “Gilded Summit” at 8%.</li>
    </ul>
    <h3 class="range-title range-title--ready">Ready to Drink</h3>
    <ul class="range-list range-list--ready">
      <li>Crafted and bottled at the source.</li>
      <li>Carbonated for the ultimate in refreshment.</li>
      <li>Available in both glass and aluminum.</li>
      <li>Two different ABV percentages to<br>choose from 5% and “Gilded Summit” at 8%.</li>
    </ul>
    <div class="photo" role="img" aria-label="Product photo of four bottles in mango, peach, watermelon and coconut flavours"></div>
  </section>

  <!-- Back -->
  <section class="panel panel--black back">
    <div class="photo" role="img" aria-label="Product photo of mango and coconut cans on a sunny beach"></div>
    <div class="stripes"></div>
    <p class="brand-name">Gilded Reef</p>
    <p class="back-contacts">Contacts...............<br>..............................<br>..............................</p>
  </section>

</body>
</html>
```